Broschüre für Gleichstellungsstelle einer kommunalen Stadtverwaltung
Zielgruppe
Wir sind die Gleichstellungsstelle einer kommunalen Stadtverwaltung (Einwohner*innen ca. 74.500) und richten uns mit unserer Arbeit grundsätzlich an alle Menschen.
Wir wollen eine Broschüre zum Handlungsleitfaden für die geschlechtergerechte Sprache bei der Stadt erstellen. Dieser soll an die Beschäftigten als Unterstützung verteilt werden.
Aufgabenstellung
- Broschüre mit Wire-O-Bindung, Druckformat 14,8 cm x 14,8 cm, Endformat 15,0 x 15,0 cm
- Spiralbindung an der Kopfseite
- doppelseitiges Deckblatt und Rückseite
- 16 Seiten Inhalt, wobei lediglich die Vorderseiten Text enthalten
- Schriftart (optimal Avenir Next, alternativ Arial) und Farbschema laut Corporate Design
- Der Text ist vorgegeben, die Gestaltung ist im Rahmen des Corporate Designs frei
Es soll eine ansprechende Broschüre gestaltet werden, welche die Leser*innen zum Blättern einlädt. Das bedeutet, dass alle Seiten (Deckblatt, Inhaltsseiten und Rückseiten) bei der Gestaltung berücksichtigt werden müssen.
Am Ende soll neben den üblichen Dateien auch eine fertige Druckdatei (siehe Datenblatt) zur Verfügung gestellt werden. Dabei ist zu beachten, dass die Spiralbindung des fertigen Produkts an der Kopfseite sein soll.

```html
<!DOCTYPE html>
<html lang="de">
<head>
<meta charset="utf-8">
<title>Akademische Grade und Titel</title>
<link rel="stylesheet" href="https://fonts.googleapis.com/css2?family=Nunito+Sans:wght@400;700;800&display=swap">
<style>
  :root {
    --green-dark: #00524a;
    --green-soft: #9bb5b0;
    --accent-light: #aac4be;
    --text-grey: #6a6a6a;
    --white: #ffffff;
    --frame: #cfcfcf;
  }
  * { margin: 0; padding: 0; box-sizing: border-box; }
  html, body { width: 1200px; height: 1200px; overflow: hidden; background: var(--white); }
  .page {
    position: relative;
    width: 1200px;
    height: 1200px;
    border: 1px solid var(--frame);
    font-family: "Nunito Sans", "Avenir Next", Arial, sans-serif;
    color: var(--text-grey);
  }
  .intro {
    position: absolute;
    left: 0; top: 0;
    width: 100%;
    height: 383px;
    background: var(--green-dark);
    color: var(--white);
    padding: 128px 0 0 81px;
  }
  .intro-title {
    font-size: 35px;
    font-weight: 800;
    letter-spacing: 0.2px;
    line-height: 1.2;
    margin-bottom: 4px;
  }
  .intro-text {
    font-size: 27px;
    line-height: 39px;
    width: 1000px;
  }
  .intro-text strong { color: var(--accent-light); font-weight: 700; }
  .title-grid {
    position: absolute;
    left: 81px;
    font-size: 28px;
    line-height: 39px;
  }
  .title-grid .col { position: absolute; top: 0; white-space: nowrap; }
  .title-grid .col-1 { left: 0; }
  .title-grid .col-2 { left: 279px; }
  .title-grid .col-3 { left: 639px; }
  .grid-explicit { top: 440px; }
  .grid-neutral { top: 772px; }
  .note-band {
    position: absolute;
    left: 0; top: 616px;
    width: 962px;
    height: 126px;
    background: var(--green-soft);
    color: var(--white);
    font-size: 27px;
    line-height: 41px;
    padding: 20px 0 0 81px;
  }
</style>
</head>
<body>
  <div class="page">
    <header class="intro">
      <h1 class="intro-title">AKADEMISCHE GRADE UND TITEL</h1>
      <p class="intro-text">Auch bei Akademischen Graden oder Titeln ist darauf zu achten, geschlechtersensibel zu formulieren.<br>Bei einzelnen bekannten Personen, können die <strong>explizit männlichen oder weiblichen Bezeichnungen</strong> gewählt werden. Zum Beispiel:</p>
    </header>

    <div class="title-grid grid-explicit">
      <div class="col col-1">Professor /<br>Professorin<br>Prof. / Prof.in</div>
      <div class="col col-2">Doktor / Doktorin<br>Dr. / Dr.in</div>
      <div class="col col-3">Diplom-Ingenieur /<br>Diplom-Ingenieurin<br>Dipl.-Ing / Dipl.-Ing.in</div>
    </div>

    <p class="note-band">Wenn das Geschlecht einer Person unbekannt ist, kann das<br>Gendersternchen verwendet werden. Zum Beispiel:</p>

    <div class="title-grid grid-neutral">
      <div class="col col-1">Professor*in<br>Prof.*in</div>
      <div class="col col-2">Doktor*in<br>Dr.*in</div>
      <div class="col col-3">Diplom-Ingenieur*in<br>Dipl.-Ing*in</div>
    </div>
  </div>
</body>
</html>
```